Real Estate Webpage Design

We have an existing website: brindlewoodhomes.com.au
We focus customised service mainly on Property Management and second-hand property sales.
We are not entirely happy about the current design and layout can stay roughly the same as the back end coding is linked to a CRM system.
We would like to see the design are more reachable to our clients and appearing.
Please check our Website Design Draft for more details.

Industry/Entity Type

Real estate Agency

Number of Pages Required

5+ page

Font styles to use
Sans Serif

Colors

Designer to choose colors to be used in the design.

```html
<!DOCTYPE html>
<html lang="en">
<head>
<meta charset="utf-8">
<title>Brindlewood — Property Group</title>
<link rel="stylesheet" href="https://fonts.googleapis.com/css2?family=Inter:wght@400;500;600;700&family=Poppins:wght@600;700;800&display=swap">
<style>
:root{
  --navy:#1d3559;
  --ink:#222831;
  --muted:#6b7480;
  --orange:#f08a4b;
  --yellow:#f7b84b;
  --dark-band:#2c3e55;
  --blue-band:#3d6b8c;
  --form-blue:#4a7b9d;
  --soft:#f2f6f8;
  --line:#e3e7eb;
  --white:#ffffff;
}
*{margin:0;padding:0;box-sizing:border-box}
html,body{width:1200px;height:4758px;overflow:hidden}
body{position:relative;font-family:"Inter",sans-serif;color:var(--ink);background:var(--white)}
.abs{position:absolute}
.heading{font-family:"Poppins",sans-serif;font-weight:700;color:var(--ink);text-align:center;font-size:29px;left:0;width:1200px}
.subheading{font-size:19px;color:#333;text-align:center;left:0;width:1200px}

/* header + hero */
.hero{left:0;top:0;width:1200px;height:665px;background:linear-gradient(160deg,#f4f6f8 0%,#e6ebef 40%,#cfdce3 70%,#8fb8c4 100%)}
.brand{left:85px;top:32px;display:flex;align-items:center;gap:12px}
.brand-mark{width:46px;height:46px;border:4px solid var(--yellow);border-radius:4px}
.brand-name{font-family:"Poppins",sans-serif;font-weight:600;font-size:36px;color:var(--orange);line-height:1}
.brand-tag{left:153px;top:72px;font-size:9px;color:var(--orange)}
.nav{left:495px;top:50px;display:flex;gap:22px;font-size:14px;font-weight:600;color:var(--ink)}
.nav .active{color:var(--orange);border-bottom:3px solid var(--orange);padding-bottom:4px}
.hero-title{left:0;width:1200px;top:258px;text-align:center;font-family:"Poppins",sans-serif;font-weight:800;font-size:40px;line-height:63px;color:var(--navy);letter-spacing:.5px}
.search{left:175px;top:391px;width:850px;height:56px;background:rgba(255,255,255,.88);border-radius:28px;border:2px solid #fff;box-shadow:0 2px 10px rgba(0,0,0,.08)}
.search .field{position:absolute;top:9px}
.search .label{font-size:14px;font-weight:700;color:var(--ink)}
.search .hint{font-size:11px;color:var(--muted);margin-top:6px}
.search .divider{position:absolute;top:8px;width:1px;height:40px;background:#d7dbe0}
.search .caret{position:absolute;top:33px;width:0;height:0;border-left:7px solid transparent;border-right:7px solid transparent;border-top:9px solid var(--orange)}
.search-btn{position:absolute;left:707px;top:5px;width:133px;height:44px;border-radius:22px;background:var(--yellow);color:#fff;font-size:14px;font-weight:700;display:flex;align-items:center;justify-content:center;gap:8px}

/* about */
.about{left:0;top:665px;width:1200px;height:570px;background:var(--soft)}
.about-frame{left:105px;top:757px;width:381px;height:336px;background:#fff;clip-path:polygon(0 16%,50% 0,100% 16%,100% 100%,0 100%)}
.about-photo{left:121px;top:773px;width:349px;height:304px;background:linear-gradient(135deg,#dcdfe2,#c7cbcf 60%,#d9b79d);clip-path:polygon(0 13%,50% 0,100% 13%,100% 100%,0 100%)}
.about-title{left:523px;top:783px;font-family:"Poppins",sans-serif;font-weight:600;font-size:29px}
.about-rule{left:523px;top:822px;width:84px;height:5px;background:var(--orange);border-radius:3px}
.about-copy{left:523px;top:847px;width:600px;font-size:19px;line-height:24px;color:#333}
.about-copy p+p{margin-top:24px}

/* achievements */
.achieve{left:0;top:1165px;width:1200px;height:293px;background:var(--dark-band);clip-path:polygon(0 0,50% 68px,100% 0,100% 100%,0 100%)}
.achieve-title{top:1270px;left:0;width:1200px;text-align:center;color:#fff;font-family:"Poppins",sans-serif;font-weight:600;font-size:28px}
.stat{top:1320px;width:260px;text-align:center}
.stat .num{font-family:"Poppins",sans-serif;font-weight:600;font-size:52px;color:var(--orange);line-height:1.2}
.stat .cap{font-size:19px;font-weight:700;color:#fff;margin-top:4px}

/* areas */
.area{width:240px;height:100px;display:flex;align-items:center;gap:20px}
.area .thumb{width:100px;height:100px;border-radius:6px;flex:none}
.area .name{font-size:17px;font-weight:700}
.area .count{font-size:16px;color:var(--muted);margin-top:12px}
.arrow{width:32px;height:32px;border-radius:50%;border:2px solid var(--orange);background:#fff;display:flex;align-items:center;justify-content:center}
.arrow svg{width:12px;height:12px;fill:var(--orange)}

/* properties */
.tabs{top:2143px;font-size:15px;font-weight:500}
.tab-active{color:var(--orange);border-bottom:3px solid var(--orange);padding-bottom:5px}
.card{width:246px;top:2197px}
.card .photo{width:246px;height:149px}
.card .fav{position:absolute;right:6px;top:6px;width:27px;height:27px;border-radius:6px;background:#f7c6c2;display:flex;align-items:center;justify-content:center}
.card .city{font-size:16px;font-weight:700;margin:12px 0 0 11px}
.card .addr{font-size:12.5px;margin:6px 0 0 11px}
.card .specs{display:flex;gap:10px;font-size:12px;color:var(--muted);margin:12px 0 0 11px;align-items:center}
.card .specs span{display:flex;align-items:center;gap:4px}
.card .specs svg{width:14px;height:12px;stroke:var(--muted);fill:none;stroke-width:1.5}
.card .rule{height:1px;background:var(--line);margin-top:12px}
.card .price{display:flex;justify-content:space-between;align-items:center;margin:10px 11px 0 11px;font-size:13.5px;font-weight:700}
.card .avatar{width:32px;height:32px;border-radius:50%}

/* explore */
.explore{left:0;top:2629px;width:1200px;height:579px;background:var(--blue-band)}
.explore-title{top:2700px;color:#fff}
.explore-sub{top:2744px;color:#e8f0f5}
.tile{top:2810px;width:192px;height:282px}
.tile .label{position:absolute;left:0;width:100%;top:180px;text-align:center;color:#fff;font-size:17px;font-weight:700}

/* blog */
.feature{left:83px;top:3410px;width:332px;height:273px;background:linear-gradient(120deg,#eef1f2,#d7dcdc 70%,#9aa3a6)}
.feature-text{left:110px;top:3452px;width:270px}
.feature .meta,.post .meta{font-size:11px;color:#555}
.feature-title{font-family:"Poppins",sans-serif;font-weight:700;font-size:19px;line-height:24px;margin-top:10px}
.feature-body{font-size:11px;line-height:13px;margin-top:10px;color:#333}
.btn-orange{display:inline-block;background:var(--yellow);color:#fff;font-size:11px;font-weight:600;padding:8px 14px;border-radius:3px;margin-top:18px}
.post{width:342px;height:123px;display:flex;gap:10px}
.post .pimg{width:123px;height:123px;flex:none}
.post .ptitle{font-size:13px;font-weight:700;line-height:16px;margin-top:6px}
.post .pbody{font-size:10px;line-height:12px;color:#555;margin-top:6px}
.post .more{font-size:10px;color:var(--orange);text-decoration:underline;margin-top:10px}

/* help */
.help-bg{left:772px;top:3849px;width:428px;height:427px;background:linear-gradient(150deg,#d9cbbd,#efe7dc 45%,#d58a4c 75%,#b8b1a6)}
.help-title{left:83px;top:3956px;font-family:"Poppins",sans-serif;font-weight:600;font-size:29px;line-height:37px}
.help-copy{left:83px;top:4058px;width:440px;font-size:19px;line-height:24px;color:#333}
.form{left:587px;top:3903px;width:312px;height:321px;background:var(--form-blue)}
.input{position:absolute;left:19px;width:265px;height:37px;background:#fff;border-radius:3px;font-size:11px;color:#888;padding:11px 12px}
.send{position:absolute;left:19px;top:254px;width:110px;height:30px;background:var(--yellow);color:#fff;font-size:11px;font-weight:600;border-radius:3px;display:flex;align-items:center;justify-content:center}

/* footer */
.footer-bg{left:0;top:4362px;width:1200px;height:396px;background:linear-gradient(135deg,#bcd3de,#dde8ee 45%,#a8c2cf)}
.footer-panel{left:44px;top:4412px;width:1112px;height:288px;background:rgba(244,247,249,.82)}
.fcol{top:4458px}
.fcol h4{font-size:16px;font-weight:500;color:var(--ink);margin-bottom:14px}
.fcol li{list-style:none;font-size:13px;line-height:26px;color:#333}
.contact{font-size:11px;color:#666;display:flex;gap:10px;align-items:flex-start;margin-bottom:14px;line-height:13px}
.contact svg{width:13px;height:13px;flex:none;stroke:#666;fill:none;stroke-width:1.5}
.socials{left:78px;top:4626px;display:flex;gap:14px}
.socials span{width:13px;height:13px;background:var(--ink);border-radius:2px}
.sub-input{left:860px;top:4499px;width:201px;height:37px;background:#fff;border-radius:3px;font-size:11px;color:#888;padding:12px 14px}
.sub-btn{left:1072px;top:4499px;width:41px;height:37px;background:var(--yellow);border-radius:3px;display:flex;align-items:center;justify-content:center}
</style>
</head>
<body>

<!-- HERO -->
<div class="abs hero" role="img" aria-label="Modern white apartment building with glass-fronted balconies against a pale sky"></div>
<div class="abs brand"><div class="brand-mark"></div><div class="brand-name">Brindlewood</div></div>
<div class="abs brand-tag">Property Group</div>
<nav class="abs nav">
  <span class="active">HOME</span><span>ABOUT US</span><span>LEASING</span><span>BUY</span><span>SELL</span><span>OUR TEAM</span><span>BLOG</span><span>CONTACT US</span>
</nav>
<h1 class="abs hero-title">PLAN YOUR FUTURE PROPERTY WITH US,<br>ARE YOU READY ?</h1>
<div class="abs search">
  <div class="field" style="left:24px"><div class="label">TYPE</div><div class="hint">Property Type</div></div>
  <div class="caret" style="left:170px"></div>
  <div class="divider" style="left:205px"></div>
  <div class="field" style="left:230px"><div class="label">LOCATION</div><div class="hint">All Cities</div></div>
  <div class="caret" style="left:340px"></div>
  <div class="divider" style="left:375px"></div>
  <div class="field" style="left:400px"><div class="label">SEARCH</div><div class="hint">Enter Keywords</div></div>
  <div class="search-btn"><svg width="16" height="16" viewBox="0 0 16 16" fill="none" stroke="#fff" stroke-width="2"><circle cx="7" cy="7" r="5"/><line x1="11" y1="11" x2="15" y2="15"/></svg>SEARCH</div>
</div>

<!-- ABOUT -->
<div class="abs about"></div>
<div class="abs about-frame"></div>
<div class="abs about-photo" role="img" aria-label="Two hands passing a small model house with a blue roof"></div>
<h2 class="abs about-title">Brindlewood</h2>
<div class="abs about-rule"></div>
<div class="abs about-copy">
  <p>Brindlewood is named for the place you call home. Buying a property is one of the most expensive expenses and important assets for people. Brindlewood is a real estate company located in Gungahlin, Canberra.</p>
  <p>Being a portfolio sales agent and property manager, coupled with our high–profile international real estate experience, Brindlewood is considered a market leader on the cutting edge with deep industry knowledge, ranging from landlord–tenant relationships, residential purchases.</p>
</div>

<!-- ACHIEVEMENTS -->
<div class="abs achieve"></div>
<h2 class="abs achieve-title">Our Achievments</h2>
<div class="abs stat" style="left:303px"><div class="num">2,763</div><div class="cap">Propreties Sold</div></div>
<div class="abs stat" style="left:621px"><div class="num">1,682</div><div class="cap">Propreties Leased</div></div>

<!-- AREAS -->
<h2 class="abs heading" style="top:1540px">Areas We Serve</h2>
<p class="abs subheading" style="top:1588px">Explore our areas to find your future property</p>
<div class="abs arrow" style="left:41px;top:1744px"><svg viewBox="0 0 12 12"><path d="M9 1 L2 6 L9 11Z"/></svg></div>
<div class="abs arrow" style="left:1123px;top:1744px"><svg viewBox="0 0 12 12"><path d="M3 1 L10 6 L3 11Z"/></svg></div>

<div class="abs area" style="left:103px;top:1645px"><div class="thumb" role="img" aria-label="Canberra city at night" style="background:linear-gradient(160deg,#1d2440,#5a3c4c 60%,#d09a4a)"></div><div><div class="name">Canberra</div><div class="count">24 Listings</div></div></div>
<div class="abs area" style="left:366px;top:1645px"><div class="thumb" role="img" aria-label="Newcastle arched bridge over the river" style="background:linear-gradient(180deg,#c5d9ea,#e7edf2 55%,#9aa2a8)"></div><div><div class="name">Newcastle</div><div class="count">24 Listings</div></div></div>
<div class="abs area" style="left:630px;top:1645px"><div class="thumb" role="img" aria-label="Los Angeles palm trees at sunset" style="background:linear-gradient(180deg,#e49a5a,#7a3f34 60%,#2a1b1d)"></div><div><div class="name">Los Angeles</div><div class="count">24 Listings</div></div></div>
<div class="abs area" style="left:892px;top:1645px"><div class="thumb" role="img" aria-label="Paris with the Eiffel Tower" style="background:linear-gradient(180deg,#a9cde8,#dbe9f4 60%,#b8aa92)"></div><div><div class="name">Paris</div><div class="count">24 Listings</div></div></div>
<div class="abs area" style="left:103px;top:1778px"><div class="thumb" role="img" aria-label="Melbourne city towers" style="background:linear-gradient(180deg,#b8cde0,#7f8f99 60%,#5d6b52)"></div><div><div class="name">Melbourne</div><div class="count">24 Listings</div></div></div>
<div class="abs area" style="left:366px;top:1778px"><div class="thumb" role="img" aria-label="London street with a red bus" style="background:linear-gradient(180deg,#d9d6d3,#b3a7a0 55%,#a23a35)"></div><div><div class="name">London</div><div class="count">24 Listings</div></div></div>
<div class="abs area" style="left:630px;top:1778px"><div class="thumb" role="img" aria-label="Auckland skyline across the harbour" style="background:linear-gradient(180deg,#b7c6c9,#d6a979 55%,#476a73)"></div><div><div class="name">Auckland</div><div class="count">24 Listings</div></div></div>
<div class="abs area" style="left:892px;top:1778px"><div class="thumb" role="img" aria-label="Miami towers and palm trees from below" style="background:linear-gradient(180deg,#f2f3f1,#a9b6b0 55%,#45584c)"></div><div><div class="name">Miami</div><div class="count">24 Listings</div></div></div>

<!-- LATEST PROPERTIES -->
<h2 class="abs heading" style="top:2040px">Our Lates Properties</h2>
<p class="abs subheading" style="top:2088px">Lorem ipsum dolor sit amet, consectetur adipiscing elit.</p>
<div class="abs tabs" style="left:475px">FOR SALE</div>
<div class="abs tabs tab-active" style="left:637px">FOR LEASE</div>
<div class="abs arrow" style="left:41px;top:2353px"><svg viewBox="0 0 12 12"><path d="M9 1 L2 6 L9 11Z"/></svg></div>
<div class="abs arrow" style="left:1123px;top:2353px"><svg viewBox="0 0 12 12"><path d="M3 1 L10 6 L3 11Z"/></svg></div>

<div class="abs card" style="left:81px">
  <div class="photo" role="img" aria-label="Bright living room with sofas and large windows" style="background:linear-gradient(135deg,#e9e4db,#c9b9a2 60%,#8a7a66)"></div>
  <div class="fav"><svg width="14" height="12" viewBox="0 0 14 12"><path d="M7 11 L1.5 5.5 A3 3 0 0 1 7 2 A3 3 0 0 1 12.5 5.5Z" fill="#fff"/></svg></div>
  <div class="city">Canberra</div><div class="addr">14 Fernleigh Street Red Hill</div>
  <div class="specs"><span><svg viewBox="0 0 14 12"><path d="M1 11V3h12v8M1 8h12"/></svg>2</span><span><svg viewBox="0 0 14 12"><path d="M1 6h12v3a2 2 0 0 1-2 2H3a2 2 0 0 1-2-2Z"/></svg>2</span><span><svg viewBox="0 0 14 12"><path d="M2 8l1-5h8l1 5v3H2Z"/></svg>2</span><span><svg viewBox="0 0 14 12"><rect x="1" y="1" width="12" height="10"/></svg>800 Sqm</span></div>
  <div class="rule"></div>
  <div class="price"><span>$379,8/mo</span><div class="avatar" role="img" aria-label="Listing agent portrait" style="background:#8fa7b8"></div></div>
</div>
<div class="abs card" style="left:345px">
  <div class="photo" role="img" aria-label="Grey living room with fireplace and shelves" style="background:linear-gradient(135deg,#d8d8d6,#8d8e8c 60%,#4b4b4a)"></div>
  <div class="fav"><svg width="14" height="12" viewBox="0 0 14 12"><path d="M7 11 L1.5 5.5 A3 3 0 0 1 7 2 A3 3 0 0 1 12.5 5.5Z" fill="#fff"/></svg></div>
  <div class="city">Melbourne</div><div class="addr">3/28 Kestrel Lane</div>
  <div class="specs"><span><svg viewBox="0 0 14 12"><path d="M1 11V3h12v8M1 8h12"/></svg>2</span><span><svg viewBox="0 0 14 12"><path d="M1 6h12v3a2 2 0 0 1-2 2H3a2 2 0 0 1-2-2Z"/></svg>2</span><span><svg viewBox="0 0 14 12"><path d="M2 8l1-5h8l1 5v3H2Z"/></svg>2</span><span><svg viewBox="0 0 14 12"><rect x="1" y="1" width="12" height="10"/></svg>910 Sqm</span></div>
  <div class="rule"></div>
  <div class="price"><span>$431,3/mo</span><div class="avatar" role="img" aria-label="Listing agent portrait" style="background:#3a3a3a"></div></div>
</div>
<div class="abs card" style="left:608px">
  <div class="photo" role="img" aria-label="White modern cube house under a clear sky" style="background:linear-gradient(180deg,#e7ecf0,#f7f7f7 55%,#b7bcbe)"></div>
  <div class="fav"><svg width="14" height="12" viewBox="0 0 14 12"><path d="M7 11 L1.5 5.5 A3 3 0 0 1 7 2 A3 3 0 0 1 12.5 5.5Z" fill="#fff"/></svg></div>
  <div class="city">Miami</div><div class="addr">NE 54th Terrace</div>
  <div class="specs"><span><svg viewBox="0 0 14 12"><path d="M1 11V3h12v8M1 8h12"/></svg>3</span><span><svg viewBox="0 0 14 12"><path d="M1 6h12v3a2 2 0 0 1-2 2H3a2 2 0 0 1-2-2Z"/></svg>5</span><span><svg viewBox="0 0 14 12"><path d="M2 8l1-5h8l1 5v3H2Z"/></svg>2</span><span><svg viewBox="0 0 14 12"><rect x="1" y="1" width="12" height="10"/></svg>2100 Sqm</span></div>
  <div class="rule"></div>
  <div class="price"><span>$1429,8/mo</span><div class="avatar" role="img" aria-label="Listing agent portrait" style="background:#b48a78"></div></div>
</div>
<div class="abs card" style="left:871px">
  <div class="photo" role="img" aria-label="Large grey family house with a green lawn" style="background:linear-gradient(180deg,#9fc3e0,#c9d3d8 45%,#5f7d4a)"></div>
  <div class="fav"><svg width="14" height="12" viewBox="0 0 14 12"><path d="M7 11 L1.5 5.5 A3 3 0 0 1 7 2 A3 3 0 0 1 12.5 5.5Z" fill="#fff"/></svg></div>
  <div class="city">Auckland</div><div class="addr">7 Harrowgate Rd</div>
  <div class="specs"><span><svg viewBox="0 0 14 12"><path d="M1 11V3h12v8M1 8h12"/></svg>3</span><span><svg viewBox="0 0 14 12"><path d="M1 6h12v3a2 2 0 0 1-2 2H3a2 2 0 0 1-2-2Z"/></svg>2</span><span><svg viewBox="0 0 14 12"><path d="M2 8l1-5h8l1 5v3H2Z"/></svg>2</span><span><svg viewBox="0 0 14 12"><rect x="1" y="1" width="12" height="10"/></svg>1800 Sqm</span></div>
  <div class="rule"></div>
  <div class="price"><span>$1352,7/mo</span><div class="avatar" role="img" aria-label="Listing agent portrait" style="background:#6b7f5a"></div></div>
</div>

<!-- EXPLORE -->
<div class="abs explore" role="img" aria-label="Blue painted brick wall"></div>
<h2 class="abs heading explore-title" style="color:#fff">Explore Our Properties</h2>
<p class="abs subheading explore-sub">Lorem ipsum dolor sit amet, consectetur adipiscing elit.</p>
<div class="abs arrow" style="left:41px;top:2932px"><svg viewBox="0 0 12 12"><path d="M9 1 L2 6 L9 11Z"/></svg></div>
<div class="abs arrow" style="left:1123px;top:2932px"><svg viewBox="0 0 12 12"><path d="M3 1 L10 6 L3 11Z"/></svg></div>
<div class="abs tile" style="left:83px" role="img" aria-label="Two-storey house with a lawn" ><div style="position:absolute;inset:0;background:linear-gradient(180deg,#8aa2b8,#6f7a82 55%,#586b3e)"></div><div class="label">House</div></div>
<div class="abs tile" style="left:293px" role="img" aria-label="Room with an orange sofa"><div style="position:absolute;inset:0;background:linear-gradient(180deg,#d6d3cc,#a9a296 55%,#b06a3e)"></div><div class="label">Room</div></div>
<div class="abs tile" style="left:504px" role="img" aria-label="Villa with a pool at dusk"><div style="position:absolute;inset:0;background:linear-gradient(180deg,#6f7f8a,#3e4a4f 55%,#50707a)"></div><div class="label">Villa</div></div>
<div class="abs tile" style="left:714px" role="img" aria-label="Apartment tower seen from below"><div style="position:absolute;inset:0;background:linear-gradient(180deg,#e4e6e7,#8a8f92 50%,#3f4447)"></div><div class="label">Apartment</div></div>
<div class="abs tile" style="left:923px" role="img" aria-label="Office with a long table and chairs"><div style="position:absolute;inset:0;background:linear-gradient(180deg,#cfd3d3,#6f6c66 55%,#4a3f38)"></div><div class="label">Office</div></div>

<!-- BLOG -->
<h2 class="abs heading" style="top:3305px">From Our Blog</h2>
<p class="abs subheading" style="top:3352px">Lorem ipsum dolor sit amet, consectetur adipiscing elit.</p>
<div class="abs feature" role="img" aria-label="Keyboard and plant on a bright desk"></div>
<div class="abs feature-text feature">
  <div class="meta">Mara Lind . 24 May . 3 min read</div>
  <div class="feature-title">How Long Does It Take<br>to Find a Tenant ?</div>
  <div class="feature-body">Lorem ipsum dolor sit amet, consectetur adipiscing elit. Morbi eget ultricies sed amet amet elementum faucibus lorem. Enim et massa volutpat at nulla tincidunt suspendisse integer massa.</div>
  <div class="btn-orange">Read More</div>
</div>
<div class="abs post" style="left:434px;top:3410px"><div class="pimg" role="img" aria-label="Small model house with keys" style="background:linear-gradient(135deg,#e6e6e4,#b7b4b0 60%,#b8443a)"></div><div><div class="meta">Paul Orrin . 08 May . 3 min read</div><div class="ptitle">For Protect Your Property</div><div class="pbody">Lorem ipsum dolor sit amet, consect adipiscing elit. Augue vel lectus mol massa id lectus.</div><div class="more">Read More</div></div></div>
<div class="abs post" style="left:785px;top:3410px"><div class="pimg" role="img" aria-label="Person working at a laptop by a window" style="background:linear-gradient(135deg,#cfdad9,#7f8b8c 60%,#2f3a44)"></div><div><div class="meta">Theo Kemp . 05 May . 3 min read</div><div class="ptitle">What You Should Know Before Start Renting ?</div><div class="pbody">Lorem ipsum dolor sit amet, consect adipiscing elit. Augue vel lectus mol massa id lectus.</div><div class="more">Read More</div></div></div>
<div class="abs post" style="left:434px;top:3559px"><div class="pimg" role="img" aria-label="Two people shaking hands in an office" style="background:linear-gradient(135deg,#dfe6ea,#8aa0b0 55%,#d27b3c)"></div><div><div class="meta">Anna Reyes . 17 May . 3 min read</div><div class="ptitle">Increase Your Housing Project Sales 3x Faster!</div><div class="pbody">Lorem ipsum dolor sit amet, consect adipiscing elit. Augue vel lectus mol massa id lectus.</div><div class="more">Read More</div></div></div>
<div class="abs post" style="left:785px;top:3559px"><div class="pimg" role="img" aria-label="Dark hallway with a lit doorway" style="background:linear-gradient(135deg,#2f3236,#4b4a44 55%,#c9a25a)"></div><div><div class="meta">Theo Kemp . 05 May . 3 min read</div><div class="ptitle">Renovating an Existing Home instead of Buying a New House</div><div class="pbody">Lorem ipsum dolor sit amet, consect adipiscing elit. Augue vel lectus mol massa id lectus.</div><div class="more">Read More</div></div></div>

<!-- HELP -->
<div class="abs help-bg" role="img" aria-label="Living room with an orange armchair and a round mirror"></div>
<h2 class="abs help-title">We Help You Buy or Sell<br>Your Property</h2>
<p class="abs help-copy">Lorem ipsum dolor sit amet, consectetur adipiscing elit. Commodo mattis feugiat morbi gravida. Consequat aliquet sitvitae quam lacus nulla cras vulputate. Leo quis egestas ultrices morbi nunc, eu.</p>
<form class="abs form">
  <div class="input" style="top:55px">Your Name</div>
  <div class="input" style="top:108px">E-mail/Phone</div>
  <div class="input" style="top:160px;height:78px">Message</div>
  <div class="send">Send Message</div>
</form>

<!-- FOOTER -->
<div class="abs footer-bg" role="img" aria-label="Glass office towers seen from below"></div>
<div class="abs footer-panel"></div>
<div class="abs fcol" style="left:78px;width:300px">
  <h4>About</h4>
  <div class="contact"><svg viewBox="0 0 14 14"><path d="M7 13s-4.5-4.5-4.5-7.5a4.5 4.5 0 0 1 9 0C11.5 8.5 7 13 7 13Z"/><circle cx="7" cy="5.5" r="1.5"/></svg><span>18/4 Marlowe Crescent,<br>Harrison, ACT, 2914</span></div>
  <div class="contact"><svg viewBox="0 0 14 14"><path d="M3 1h3l1 3-2 1a8 8 0 0 0 4 4l1-2 3 1v3a1 1 0 0 1-1 1A11 11 0 0 1 2 2a1 1 0 0 1 1-1Z"/></svg><span>02 6188 2350</span></div>
  <div class="contact"><svg viewBox="0 0 14 14"><rect x="1" y="3" width="12" height="8"/><path d="M1 3l6 5 6-5"/></svg><span>hello@brindlewoodhomes.com.au</span></div>
</div>
<div class="abs socials"><span></span><span></span><span></span><span></span></div>
<div class="abs fcol" style="left:421px"><h4>Discover</h4><ul><li>Canberra</li><li>Melbourne</li><li>Perth</li><li>Newcastle</li></ul></div>
<div class="abs fcol" style="left:541px"><h4>Lists by Category</h4><ul><li>House</li><li>Room</li><li>Apartment</li><li>Villa</li><li>Office</li></ul></div>
<div class="abs fcol" style="left:718px"><h4>Quick Access</h4><ul><li>About Us</li><li>Leasing</li><li>Buy</li><li>Sell</li><li>Our Team</li><li>Blog</li></ul></div>
<div class="abs fcol" style="left:860px"><h4>Subscribe</h4></div>
<div class="abs sub-input">Your E-mail</div>
<div class="abs sub-btn"><svg width="18" height="18" viewBox="0 0 18 18"><path d="M1 8 L17 1 L11 17 L8 10Z" fill="#fff"/></svg></div>

</body>
</html>
```